Wix Website design for my therapy business - Willowmere Group

I have started designing a Wix site and have a good idea of what I want.
I have set up the pages, created some design ideas, and inputted the copy. I need someone fabulous to finish off the design aspects. I like working closely with the designers, I was an interior designer in an old career.
I would like the site to be funky but professional. My Wix skills are limited, and I just can't achieve the look I am wanting without having to spend a lot of time learning. If it's easier to start over, that's ok providing you use the same colours, font, images etc. I have included a screenshot of the home page below. I have another site I need to start as soon as we have finished this one.
I am looking for someone who is a good listener and is has design flare. I am easy to get along with and will respond quickly.
I would like to set up SEO and have help in the future.
Let me know if you are the right person for the job.
Target Market(s)
Please needing help with their mental health and for therapy.
Industry/Entity Type
Mental health
Font styles to use
Other font styles liked:
- Futura light
Requirements
Must have
- be easy to navigate and be simple yet stylish
Nice to have
- I have set up the basics of the site - nice to haves are already on the site
Should not have
- old fashioned large chunks of text.

```html
<!DOCTYPE html>
<html lang="en">
<head>
<meta charset="UTF-8">
<title>Willowmere Group – Mental Health Redefined</title>
<link rel="stylesheet" href="https://fonts.googleapis.com/css2?family=Playfair+Display:wght@400&family=Poppins:wght@300;400;500;600&display=swap">
<style>
:root{
  --brown:#8a6c4d;
  --brown-soft:#a98e72;
  --blue:#1a5c87;
  --ink:#3b3b3b;
  --muted:#7a7a7a;
  --cream:#f6f3ee;
  --cream-dark:#efebe4;
  --white:#ffffff;
  --line:#9cc3d8;
}
*{box-sizing:border-box;margin:0;padding:0}
html,body{width:1200px;height:3109px;overflow:hidden}
body{position:relative;background:var(--white);font-family:'Poppins',sans-serif;color:var(--ink)}
.abs{position:absolute}
h1,h2,h3,h4{font-weight:400}
.serif{font-family:'Playfair Display',serif;font-weight:400;color:var(--brown)}

/* header */
.site-header{left:0;top:0;width:1200px;height:124px;background:var(--white)}
.brand{left:0;width:1200px;top:28px;text-align:center;font-size:30px;font-weight:500;color:var(--brown);letter-spacing:.5px}
.main-nav{left:0;width:1200px;top:96px;display:flex;justify-content:center;gap:30px;font-size:11px;color:var(--ink)}
.main-nav .active{color:var(--blue);font-weight:500}

/* hero */
.hero{left:0;top:124px;width:1200px;height:446px;background:linear-gradient(180deg,#d9c6b4 0%,#e6d4c2 40%,#cbb592 75%,#d8c6a6 100%)}
.hero-shade{left:0;top:124px;width:1200px;height:446px;background:radial-gradient(ellipse at 50% 40%,rgba(246,236,226,.65),rgba(246,236,226,.1) 70%)}
.hero-title{left:0;width:1200px;top:248px;text-align:center;font-size:40px}
.hero-text{left:400px;width:400px;top:304px;text-align:center;font-size:12px;line-height:19px;color:#3a3a3a}
.btn{display:flex;align-items:center;justify-content:center;border-radius:20px;font-size:12px;height:34px}
.btn-solid{background:var(--blue);color:var(--white)}
.btn-outline{border:2px solid var(--blue);color:var(--blue);background:transparent}
.social-dot{width:32px;height:32px;border-radius:50%;background:var(--white);opacity:.9}
.chat{left:1048px;top:455px}

/* help */
.help-bg{left:0;top:567px;width:1200px;height:400px;background:var(--cream)}
.section-title{left:0;width:1200px;text-align:center;font-size:31px}
.service-card{width:215px;height:284px;background:var(--white);border-radius:10px;box-shadow:0 4px 14px rgba(0,0,0,.08)}
.service-card .photo{position:absolute;left:19px;top:19px;width:176px;height:181px;border-radius:6px}
.service-card h3{position:absolute;left:19px;top:207px;font-size:16px;font-weight:500;color:var(--blue)}
.service-card p{position:absolute;left:19px;top:236px;width:185px;font-size:11.5px;line-height:19px;color:var(--muted)}
.arrow-btn{width:38px;height:38px;border-radius:50%;display:flex;align-items:center;justify-content:center}
.arrow-btn.on{border:2px solid var(--blue)}
.arrow-btn.off{border:2px solid #d9d2c8}

/* split sections */
.feature-photo{border-radius:8px}
.photo-shadow{background:#e4ebf0;border-radius:8px}
.feature-title{font-size:29px;line-height:38px}
.body-copy{font-size:11.5px;line-height:19px;color:var(--muted)}
.perk{width:90px;text-align:center;font-size:10px;line-height:15px;color:var(--muted)}
.perk svg{display:block;margin:0 auto 6px}
.bullet{font-size:11.5px;font-weight:600;color:var(--brown)}

/* reviews */
.reviews-bg{left:0;top:1963px;width:1200px;height:460px;background:var(--cream)}
.review-card{width:213px;height:285px;background:linear-gradient(180deg,#fbfaf7,#f2efe9);border-radius:8px;box-shadow:0 4px 14px rgba(0,0,0,.07)}
.review-card .avatar{position:absolute;left:16px;top:55px;width:44px;height:44px;border-radius:50%}
.review-card .name{position:absolute;left:75px;top:62px;font-size:11px;color:var(--ink)}
.review-card .stars{position:absolute;left:75px;top:78px;font-size:12px;letter-spacing:2px;color:#111}
.review-card p{position:absolute;left:19px;top:122px;width:180px;font-size:11.5px;line-height:19px;color:var(--muted)}

/* newsletter */
.newsletter{left:0;top:2400px;width:1200px;height:372px;background:linear-gradient(180deg,#c9c1b9 0%,#d6cabc 45%,#cdbfae 100%)}
.newsletter-glow{left:0;top:2400px;width:1200px;height:372px;background:radial-gradient(ellipse at 50% 65%,rgba(255,246,230,.8),rgba(255,246,230,0) 55%)}
.news-title{left:0;width:1200px;top:2606px;text-align:center;font-size:24px;font-weight:400;letter-spacing:1.5px;color:#2e2e2e}
.news-sub{left:0;width:1200px;top:2647px;text-align:center;font-size:11.5px;color:#333}
.email-field{left:368px;top:2689px;width:380px;height:32px;border-radius:16px;background:var(--white);font-size:11px;color:#999;padding:8px 20px}
.subscribe{left:731px;top:2689px;width:100px;height:32px;border-radius:16px;background:var(--blue);color:var(--white);font-size:12px;font-weight:600}

/* footer */
.site-footer{left:0;top:2772px;width:1200px;height:337px;background:var(--cream)}
.footer-brand{left:229px;top:2840px;font-size:21px;font-weight:500;color:var(--brown)}
.footer-social{width:30px;height:30px;border-radius:50%;background:var(--brown-soft)}
.footer-col h4{font-size:14px;font-weight:500;color:var(--brown);margin-bottom:9px}
.footer-col li{list-style:none;font-size:12.5px;line-height:25px;color:#333}
.footer-col li::before{content:"•";margin-right:9px}
.footer-rule{left:0;top:3075px;width:1200px;height:1px;background:var(--line)}
.footer-url{left:0;width:1200px;top:3085px;text-align:center;font-size:11px;color:#b6a894}
</style>
</head>
<body>

<header class="abs site-header">
  <div class="abs brand">Willowmere Group</div>
  <nav class="abs main-nav">
    <span class="active">Home</span><span>About Us</span><span>EMDR</span><span>Addictions</span><span>Betrayal Trauma</span><span>PTSD</span><span>Program List</span><span>Resources</span><span>Blog</span><span>Contact Us</span>
  </nav>
</header>

<section>
  <div class="abs hero" role="img" aria-label="Photo of a woman with long hair, arms stretched wide, facing a sunlit green valley"></div>
  <div class="abs hero-shade"></div>
  <h1 class="abs serif hero-title">Mental Health Redefined</h1>
  <p class="abs hero-text">Lorem ipsum dolor sit amet, consectetur adipiscing elit, sed do eiusmod tempor incididunt ut labore et dolore magna aliqua.</p>
  <div class="abs btn btn-solid" style="left:416px;top:373px;width:175px">Get In Touch</div>
  <div class="abs btn btn-outline" style="left:604px;top:373px;width:175px">Learn More</div>
  <div class="abs social-dot" style="left:1062px;top:264px" aria-label="Social link one"></div>
  <div class="abs social-dot" style="left:1062px;top:309px" aria-label="Social link two"></div>
  <div class="abs social-dot" style="left:1062px;top:353px" aria-label="Social link three"></div>
  <svg class="abs chat" width="46" height="46" viewBox="0 0 46 46" aria-label="Chat">
    <path d="M23 2a21 21 0 1 0 12 38l8 4-3-9A21 21 0 0 0 23 2z" fill="#fff"/>
    <rect x="15" y="20" width="16" height="2.5" fill="#333"/><rect x="19" y="25" width="12" height="2.5" fill="#333"/>
  </svg>
  <svg class="abs" style="left:0;top:480px" width="1200" height="92" viewBox="0 0 1200 92">
    <path d="M0,3 Q600,171 1200,3 V92 H0 Z" fill="var(--cream)"/>
  </svg>
  <svg class="abs" style="left:589px;top:506px" width="22" height="30" viewBox="0 0 22 30" aria-label="Scroll down">
    <rect x="1.5" y="1.5" width="19" height="27" rx="9.5" fill="none" stroke="#fff" stroke-width="1.8"/>
    <path d="M11 8v12M7 16l4 4 4-4" fill="none" stroke="#fff" stroke-width="1.8"/>
  </svg>
</section>

<section>
  <div class="abs help-bg"></div>
  <svg class="abs" style="left:0;top:930px" width="1200" height="40" viewBox="0 0 1200 40">
    <path d="M0,36 Q600,-14 1200,36 V40 H0 Z" fill="var(--white)"/>
  </svg>
  <h2 class="abs serif section-title" style="top:603px">How Can We Help You?</h2>
  <div class="abs arrow-btn off" style="left:174px;top:793px"><svg width="12" height="14" viewBox="0 0 12 14"><path d="M8 2L3 7l5 5" fill="none" stroke="#d9d2c8" stroke-width="1.8"/></svg></div>
  <div class="abs arrow-btn on" style="left:988px;top:793px"><svg width="12" height="14" viewBox="0 0 12 14"><path d="M4 2l5 5-5 5" fill="none" stroke="var(--blue)" stroke-width="1.8"/></svg></div>
  <article class="abs service-card" style="left:232px;top:670px">
    <div class="photo" role="img" aria-label="Photo of a distressed woman covering her face" style="background:linear-gradient(160deg,#8d9294,#5f6466)"></div>
    <h3>Depression &rsaquo;</h3>
    <p>Lorem ipsum dolor sit amet, consectetur adipiscing elit,</p>
  </article>
  <article class="abs service-card" style="left:492px;top:670px">
    <div class="photo" role="img" aria-label="Photo of a worried man leaning against a wall" style="background:linear-gradient(160deg,#eceef0,#b9bdc3)"></div>
    <h3>Anxiety &rsaquo;</h3>
    <p>Lorem ipsum dolor sit amet, consectetur adipiscing elit,</p>
  </article>
  <article class="abs service-card" style="left:753px;top:670px">
    <div class="photo" role="img" aria-label="Photo of a therapist taking notes with a client" style="background:linear-gradient(160deg,#efefef,#c9ccc8)"></div>
    <h3>PTSD &rsaquo;</h3>
    <p>Lorem ipsum dolor sit amet, consectetur adipiscing elit,</p>
  </article>
</section>

<section>
  <div class="abs photo-shadow" style="left:164px;top:1077px;width:415px;height:332px"></div>
  <div class="abs feature-photo" role="img" aria-label="Photo of a group therapy session in a bright living room" style="left:152px;top:1065px;width:415px;height:332px;background:linear-gradient(135deg,#a5603f 0%,#d8d8d4 35%,#8d8a80 70%,#2f2f2f 100%)"></div>
  <h2 class="abs serif feature-title" style="left:620px;top:1068px">Mental Health Services,<br>Whenever You Need</h2>
  <p class="abs body-copy" style="left:620px;top:1162px;width:345px">Lorem ipsum dolor sit amet, consectetur adipiscing elit, sed do eiusmod tempor incididunt ut labore et dolore magna aliqua. Quis ipsum suspendisse ultrices gravida.</p>
  <div class="abs perk" style="left:598px;top:1252px">
    <svg width="32" height="32" viewBox="0 0 32 32"><circle cx="16" cy="14" r="11" fill="none" stroke="var(--brown)" stroke-width="1.4"/><path d="M10 28h12M16 25v3" stroke="var(--brown)" stroke-width="1.4"/><circle cx="16" cy="13" r="4" fill="none" stroke="var(--brown)" stroke-width="1.4"/></svg>
    Mental<br>Wellness</div>
  <div class="abs perk" style="left:697px;top:1252px">
    <svg width="32" height="32" viewBox="0 0 32 32"><circle cx="16" cy="7" r="3" fill="none" stroke="var(--brown)" stroke-width="1.4"/><path d="M16 12c-5 0-9 5-9 9h18c0-4-4-9-9-9zM4 26h24" fill="none" stroke="var(--brown)" stroke-width="1.4"/></svg>
    Spiritual<br>Wellness</div>
  <div class="abs perk" style="left:801px;top:1252px">
    <svg width="32" height="32" viewBox="0 0 32 32"><path d="M16 28S3 19 3 11a6.5 6.5 0 0 1 13-2 6.5 6.5 0 0 1 13 2c0 8-13 17-13 17z" fill="none" stroke="var(--brown)" stroke-width="1.4"/><circle cx="16" cy="14" r="4" fill="none" stroke="var(--brown)" stroke-width="1.4"/></svg>
    Beyond<br>Psychotherapy</div>
  <div class="abs btn btn-outline" style="left:619px;top:1357px;width:176px">Get In Touch</div>
</section>

<section>
  <h2 class="abs serif feature-title" style="left:232px;top:1524px">We Treat Because<br>We Care</h2>
  <p class="abs body-copy" style="left:232px;top:1616px;width:335px">Lorem ipsum dolor sit amet, consectetur adipiscing elit, sed do eiusmod tempor incididunt ut labore et dolore magna aliqua.</p>
  <div class="abs bullet" style="left:232px;top:1700px">• Lorem ipsum elit</div>
  <div class="abs bullet" style="left:394px;top:1700px">• Consectetur incididunt</div>
  <div class="abs bullet" style="left:232px;top:1736px">• Tempor et dolore</div>
  <div class="abs bullet" style="left:394px;top:1736px">• Dolore magna aliqua</div>
  <div class="abs btn btn-outline" style="left:232px;top:1791px;width:173px">View Program List</div>
  <div class="abs photo-shadow" style="left:631px;top:1523px;width:415px;height:331px"></div>
  <div class="abs feature-photo" role="img" aria-label="Photo of a counselor with a clipboard listening to a client on a sofa" style="left:619px;top:1511px;width:415px;height:331px;background:linear-gradient(135deg,#c6ab90 0%,#e7e2da 40%,#3c3f4a 75%,#b9c7c1 100%)"></div>
</section>

<section>
  <div class="abs reviews-bg"></div>
  <h2 class="abs serif section-title" style="top:2011px">Client Reviews</h2>
  <div class="abs arrow-btn off" style="left:231px;top:2220px"><svg width="12" height="14" viewBox="0 0 12 14"><path d="M8 2L3 7l5 5" fill="none" stroke="#d9d2c8" stroke-width="1.8"/></svg></div>
  <div class="abs arrow-btn on" style="left:281px;top:2220px"><svg width="12" height="14" viewBox="0 0 12 14"><path d="M4 2l5 5-5 5" fill="none" stroke="var(--blue)" stroke-width="1.8"/></svg></div>
  <article class="abs review-card" style="left:354px;top:2097px">
    <div class="avatar" role="img" aria-label="Portrait of Amber" style="background:linear-gradient(135deg,#3a3430,#b49a7c)"></div>
    <div class="name">Amber</div><div class="stars">★★★★★</div>
    <p>Lorem ipsum dolor sit amet, consectetur adipiscing elit, sed do eiusmod tempor incididunt ut labore.</p>
  </article>
  <article class="abs review-card" style="left:593px;top:2097px">
    <div class="avatar" role="img" aria-label="Portrait of James" style="background:linear-gradient(135deg,#9fb6c4,#d9cfc2)"></div>
    <div class="name">James</div><div class="stars">★★★★★</div>
    <p>Eli sed do eiusmod tempor incididunt ut labore et dolore magna aliqua.</p>
  </article>
  <article class="abs review-card" style="left:833px;top:2097px">
    <div class="avatar" role="img" aria-label="Portrait of Hillary" style="background:linear-gradient(135deg,#2d2a2c,#7a8fb2)"></div>
    <div class="name">Hillary</div><div class="stars">★★★★★</div>
    <p>Adipiscing elit, sed do eiusmod tempor incididunt ut labore et dolore magna aliqua.</p>
  </article>
</section>

<section>
  <div class="abs newsletter" role="img" aria-label="Silhouette of a person with raised arms against a hazy sunset"></div>
  <div class="abs newsletter-glow"></div>
  <svg class="abs" style="left:0;top:2400px" width="1200" height="100" viewBox="0 0 1200 100">
    <path d="M0,0 H1200 V14 Q600,182 0,14 Z" fill="var(--cream)"/>
  </svg>
  <h2 class="abs news-title">NEVER MISS OUT ON MENTAL WELLBEING TIPS &amp; TRICKS</h2>
  <p class="abs news-sub">Subscribe and stay up to date with our blogposts, news and more</p>
  <div class="abs email-field">Email Address</div>
  <div class="abs btn subscribe">Subscribe</div>
</section>

<footer>
  <div class="abs site-footer"></div>
  <div class="abs footer-brand">Willowmere Group</div>
  <div class="abs footer-social" style="left:235px;top:2907px" aria-label="Social link one"></div>
  <div class="abs footer-social" style="left:283px;top:2907px" aria-label="Social link two"></div>
  <div class="abs footer-social" style="left:330px;top:2907px" aria-label="Social link three"></div>
  <div class="abs footer-col" style="left:469px;top:2864px">
    <h4>Company</h4>
    <ul><li>About Us</li><li>Blog</li><li>Contact Us</li></ul>
  </div>
  <div class="abs footer-col" style="left:632px;top:2864px">
    <h4>Get Help</h4>
    <ul><li>Support Center</li><li>EMDR</li><li>Addictions</li><li>Betrayal Trauma</li><li>PTSD</li></ul>
  </div>
  <div class="abs footer-col" style="left:805px;top:2864px">
    <h4>Support</h4>
    <ul><li>Program List</li><li>Resources</li><li>FAQ</li><li>Privacy Policy</li><li>Business</li></ul>
  </div>
  <div class="abs footer-rule"></div>
  <div class="abs footer-url">www.willowmeregroup.com</div>
</footer>

</body>
</html>
```